Business card design for new eCommerce site focusing on integrity and strong businsess tactics

We need a business card that will stand out and be memorable. Something with color that matches our company logo colors. Think high end version of Dealvine. There are 2 logos provided. The parent company is called Bright Harbor Ventures and we are presenting a new and very exciting eCommerce site called KeenTraders.example.

Target Market(s)

Our target markets are in the Activities, Food and Beverage, Health and Beauty

Industry/Entity Type

Marketing

Contact Information for Business Card

We have 4 members that need cards...I will provide all info to the winner of the design contest
Business Address is
48730 West 61st Avenue, Suite C204
Phoenix AZ 85917

Font styles to use
Serif
Sans Serif

Colors

Designer to choose colors to be used in the design.

Requirements
Must have
• The card must be memorable...should be unique in design but must exude integrity and be playful .
• I have provided several colors or our parent company...please feel free to use which ever
Nice to have
• I will leave this up to you. Feel free to use other images of your choosing that wraps around our client.....Activities, Dining, Health, Beauty
Should not have
• just dont be boring

```html
<!DOCTYPE html>
<html lang="en">
<head>
<meta charset="utf-8">
<title>KeenTraders.example Business Cards</title>
<link rel="stylesheet" href="https://fonts.googleapis.com/css2?family=Open+Sans:wght@400;600;700&family=Arimo:wght@700&display=swap">
<style>
  :root {
    --backdrop: #3a3533;
    --card: #141414;
    --card-edge: #1d1d1d;
    --emboss: #3b3b3b;
    --emboss-light: #5a5a5a;
    --muted: #8a8a8a;
    --green: #8cc63f;
    --blue: #2aa3d8;
    --text: #f2f2f2;
  }
  * { box-sizing: border-box; margin: 0; padding: 0; }
  html, body { width: 1200px; height: 864px; overflow: hidden; }
  body {
    background: var(--backdrop);
    font-family: "Open Sans", Arial, sans-serif;
    position: relative;
  }
  .card {
    position: absolute;
    width: 540px;
    height: 309px;
    background: var(--card);
    border: 1px solid var(--card-edge);
    border-radius: 3px;
    box-shadow: 0 10px 24px rgba(0,0,0,.45);
    overflow: hidden;
  }
  /* Back of card: parent company */
  .card--back { left: 40px; top: 170px; }
  .parent-mark {
    position: absolute;
    left: 50%; top: 58px;
    transform: translateX(-50%);
    width: 96px; height: 96px;
    border-radius: 50%;
    background: radial-gradient(circle at 40% 35%, var(--emboss-light), var(--emboss));
  }
  .parent-name {
    position: absolute;
    left: 0; right: 0; top: 172px;
    text-align: center;
    font-family: "Arimo", Arial, sans-serif;
    font-weight: 700;
    font-size: 30px;
    color: var(--emboss-light);
  }
  .parent-url {
    position: absolute;
    left: 0; right: 0; top: 230px;
    text-align: center;
    font-size: 13px;
    letter-spacing: 3px;
    color: var(--muted);
  }
  /* Front of card: client site */
  .card--front { left: 620px; top: 380px; }
  .brand {
    position: absolute;
    left: 130px; top: 62px;
    display: flex; align-items: center; gap: 12px;
  }
  .brand-dot {
    width: 34px; height: 34px; border-radius: 50%;
    background: var(--green);
  }
  .brand-name {
    font-weight: 700; font-size: 30px; color: var(--green);
    letter-spacing: -.5px;
  }
  .brand-tagline {
    position: absolute;
    left: 178px; top: 106px;
    font-size: 13px; letter-spacing: 1.5px;
    color: var(--muted);
  }
  .contact {
    position: absolute;
    top: 168px; left: 0; right: 0;
    display: flex; justify-content: center;
  }
  .person {
    text-align: right;
    padding-right: 16px;
    font-size: 13px; line-height: 18px;
    color: var(--text);
  }
  .person-name { color: var(--blue); font-weight: 600; }
  .person-title { color: var(--green); font-weight: 600; }
  .divider { width: 1px; background: #cfcfcf; }
  .lines {
    list-style: none;
    padding-left: 16px;
    font-size: 13px; line-height: 18px; color: var(--text);
  }
  .lines li { display: flex; align-items: center; gap: 8px; }
  .lines svg { width: 11px; height: 11px; fill: var(--text); }
</style>
</head>
<body>
  <section class="card card--back" aria-label="Parent company card">
    <div class="parent-mark"></div>
    <div class="parent-name">Bright Harbor Ventures</div>
    <div class="parent-url">www.keentraders.example</div>
  </section>

  <section class="card card--front" aria-label="KeenTraders.example card">
    <div class="brand">
      <span class="brand-dot"></span>
      <span class="brand-name">KeenTraders.example</span>
    </div>
    <div class="brand-tagline">Outings-Meals-Wellness-Style</div>

    <div class="contact">
      <div class="person">
        <div class="person-name">ALEX ROWAN</div>
        <div class="person-title">CEO/FOUNDER</div>
        <div>4120 Linden Court</div>
        <div>Flagstaff, Arizona 86011</div>
      </div>
      <div class="divider"></div>
      <ul class="lines">
        <li><svg viewBox="0 0 12 12"><path d="M1 4c0-2 2-3 5-3s5 1 5 3v1H8V4H4v1H1zM2 6h8l1 5H1z"/></svg>555 203 7711</li>
        <li><svg viewBox="0 0 12 12"><path d="M3 0h6v12H3zM4 1v8h4V1z"/></svg>555 309 4826</li>
        <li><svg viewBox="0 0 12 12"><path d="M3 0h6v4H3zM1 4h10v6H1zM3 10h6v2H3z"/></svg>555 417 6052</li>
        <li><svg viewBox="0 0 12 12"><path d="M0 2h12v1L6 7 0 3zM0 4l6 4 6-4v6H0z"/></svg>alex@keentraders.example</li>
      </ul>
    </div>
  </section>
</body>
</html>
```